Letterhead & Business Card Design Project

Use existing logo to create a new letterhead and business card design. Looking for something clean modern using color options of black, white and gray. The green from the logo may be used lightly as an accent color.

Target Market(s)

Professional business people

Industry/Entity Type

Business

Requirements
Must have
• Business card with front and back design using existing logo.
Nice to have
• Professional presentation
Clean look
Should not have
• No oil rigs, pumpjacks or clip art.

```html
<!DOCTYPE html>
<html lang="en">
<head>
<meta charset="utf-8">
<title>Halvern Exploration – Business Card</title>
<link rel="stylesheet" href="https://fonts.googleapis.com/css2?family=Mulish:wght@400;800&display=swap">
<style>
  :root {
    --backdrop: #2b2b2b;
    --card-white: #f7f7f5;
    --card-black: #0b0b0b;
    --ink: #161616;
    --ink-soft: #555555;
    --accent: #2bb52b;
    --stripe-gray: #9a9a9a;
    --paper-white: #ffffff;
  }
  * { box-sizing: border-box; margin: 0; padding: 0; }
  html, body { width: 1200px; height: 800px; overflow: hidden; }
  body {
    background: var(--backdrop);
    font-family: "Mulish", sans-serif;
    position: relative;
  }
  .card {
    position: absolute;
    top: 252px;
    width: 520px;
    height: 297px;
    overflow: hidden;
  }
  .card--front { left: 50px; background: var(--card-white); color: var(--ink); }
  .card--back { left: 630px; background: var(--card-black); color: var(--paper-white); }

  .accent-bar {
    position: absolute;
    width: 10px;
    background: var(--accent);
  }
  .card--front .accent-bar { left: 0; top: 50px; height: 92px; }
  .card--back .accent-bar { right: 0; top: 28px; height: 62px; }

  .gray-stripe {
    position: absolute;
    bottom: 0;
    height: 12px;
    background: var(--stripe-gray);
  }
  .card--front .gray-stripe { right: 0; width: 225px; }
  .card--back .gray-stripe { left: 0; width: 225px; }

  .holder { position: absolute; left: 40px; top: 56px; }
  .holder__name { font-weight: 800; font-size: 19px; letter-spacing: 0.2px; }
  .holder__title { font-size: 14px; margin-top: 2px; padding-left: 4px; color: var(--ink); }

  .wordmark {
    position: absolute;
    font-weight: 400;
    font-size: 26px;
    letter-spacing: 1.5px;
    white-space: nowrap;
  }
  .card--front .wordmark { right: 26px; top: 40px; color: var(--ink); }
  .card--back .wordmark { left: 50%; top: 50%; transform: translate(-50%, -50%); font-size: 30px; color: var(--paper-white); }

  .contact { position: absolute; left: 40px; top: 168px; font-size: 13px; line-height: 16px; }
  .contact__label { color: var(--accent); }
  .address { position: absolute; left: 40px; top: 226px; font-size: 13px; line-height: 16px; }

  .website {
    position: absolute;
    font-size: 12px;
    letter-spacing: 0.2px;
  }
  .website strong { font-weight: 800; color: var(--accent); }
  .card--front .website { right: 24px; bottom: 22px; }
  .card--back .website { left: 22px; bottom: 22px; color: var(--paper-white); }
</style>
</head>
<body>
  <section class="card card--front" aria-label="Business card front">
    <span class="accent-bar"></span>
    <div class="holder">
      <p class="holder__name">Grant T Holloway</p>
      <p class="holder__title">Managing Member</p>
    </div>
    <p class="wordmark">Halvern Exploration</p>
    <div class="contact">
      <p><span class="contact__label">Phone:</span> 555.210.4471</p>
      <p><span class="contact__label">Cell:</span> 555.318.9052</p>
      <p><span class="contact__label">Fax:</span> 555.210.4472</p>
    </div>
    <div class="address">
      <p>4420 North Ridge Ave</p>
      <p>Suite 210, Westfield</p>
      <p>Kansas 66012</p>
    </div>
    <p class="website">www.<strong>halvernexploration</strong>.com</p>
    <span class="gray-stripe"></span>
  </section>

  <section class="card card--back" aria-label="Business card back">
    <span class="accent-bar"></span>
    <p class="wordmark">Halvern Exploration</p>
    <p class="website">www.<strong>halvernexploration</strong>.com</p>
    <span class="gray-stripe"></span>
  </section>
</body>
</html>
```